We need motivational posters designed to be used in classrooms at a truck driving school. The purpose of the posters is to motivate the students.

I want the the quotes to be the main focal point of emphasis and our logo on the bottom of the poster for branding purposes.

I would like the images to be related to the trucking industry

Below are the quotes for the posters

Poster 1
"Start where you are. Use what you have. Do what you can."
-Dorian Vell-

Poster 2
"The secret of getting ahead is getting started"
-Lewis Crane-

Poster 3
"Most effective way to do it, is to do it."
-Odessa Brindle-

Poster 4
"Set your goals big, and don't stop till you get there."
-Cy Morrow-

Poster 5
"If you are not willing to learn, no one can help you. If you are determined to learn, no one can stop you."
-Unknown-

Poster 6
"The will to succeed is important, but what's more important is the will to prepare."
-Teddy Sloane-

THESE POSTERS SHOULD BE DESIGNED AS 18X24
LANDSCAPE AND PORTRAIT ORIENTATION

```html
<!DOCTYPE html>
<html lang="en">
<head>
<meta charset="utf-8">
<title>Poster – Determined to Learn</title>
<link rel="stylesheet" href="https://fonts.googleapis.com/css2?family=Bodoni+Moda:wght@700&family=Montserrat:wght@400&display=swap">
<style>
  :root {
    --sky-top: #68d6b0;
    --sky-mid: #a9dca6;
    --horizon: #e6dc9e;
    --sand: #e9c58f;
    --sand-shade: #cfa672;
    --brush: #6c8f5a;
    --road: #3e4656;
    --road-dark: #2c3340;
    --text-light: #ffffff;
    --paper: #ffffff;
    --brand: #e5a41c;
    --ink: #141414;
  }
  html, body {
    margin: 0;
    padding: 0;
    overflow: hidden;
    background: var(--paper);
  }
  .poster {
    position: relative;
    width: 900px;
    height: 1200px;
    overflow: hidden;
    background: var(--paper);
  }
  .scene {
    position: absolute;
    left: 0;
    top: 0;
    width: 900px;
    height: 1100px;
    background:
      linear-gradient(180deg,
        var(--sky-top) 0%,
        var(--sky-mid) 22%,
        var(--horizon) 38%,
        var(--sand) 46%,
        var(--sand) 62%,
        var(--road) 72%,
        var(--road-dark) 100%);
  }
  .quote {
    position: absolute;
    left: 40px;
    top: 68px;
    margin: 0;
    font-family: "Bodoni Moda", "Didot", serif;
    font-weight: 700;
    font-size: 41px;
    line-height: 55px;
    color: var(--text-light);
    letter-spacing: 0.2px;
  }
  .quote-author {
    position: absolute;
    left: 41px;
    top: 326px;
    margin: 0;
    font-family: "Montserrat", "Helvetica", sans-serif;
    font-weight: 400;
    font-size: 21px;
    letter-spacing: 1.5px;
    color: var(--text-light);
  }
  .brand-band {
    position: absolute;
    left: 0;
    top: 1100px;
    width: 900px;
    height: 100px;
    background: var(--paper);
  }
  .brand {
    position: absolute;
    left: 40px;
    top: 20px;
    display: flex;
    align-items: center;
    gap: 10px;
  }
  .brand-mark {
    width: 58px;
    height: 58px;
    border-radius: 50%;
    background: var(--ink);
  }
  .brand-name {
    font-family: "Bodoni Moda", "Didot", serif;
    font-weight: 700;
    font-size: 24px;
    color: var(--brand);
    line-height: 1;
  }
</style>
</head>
<body>
  <main class="poster">
    <div class="scene" role="img" aria-label="Desert highway with a double yellow centre line winding between sand dunes and scrub under a clear teal sky"></div>

    <blockquote class="quote">
      If you are not willing to learn,<br>
      no one can help you.<br>
      If you are determined to learn,<br>
      no one can stop you.
    </blockquote>
    <p class="quote-author">UNKNOWN</p>

    <footer class="brand-band">
      <div class="brand">
        <span class="brand-mark"></span>
        <span class="brand-name">Summit Haul Driving School</span>
      </div>
    </footer>
  </main>
</body>
</html>
```